Thorne Legal PC business card. National Consumer Law Firm with principal office in San Francisco. We maintain additional offices in Meridian, Mississippi and Birmingham, Alabama. We protect consumers against unscrupulous mega corporations. We want to covey integrity and a willingness to take on the Goliaths of the corporate world. I like red accents. Try to use uploaded picture of Harbor Arch Span or a sketch. Licensed in California, Alabama and Mississippi. Main office: 318 Alder Ave. #407, San Francisco, CA 94110, ph. 415/555-0182, 800/555-0147 (fax), 205/555-0136 (AL).
www.thornelegalpc.example
www.claimwatch.example.
At top--Public Claim Advocacy in red. Also Thorne Legal PC at top in red. Then red horizontal line please. Or if you have another idea. I have not seen new logo.
After line on left at top
H. Dwight Thorne
Attorney
Cell 205/555-0194
dwight@thornelegalpc.example
Offices: San Francisco, CA, Birmingham, AL, Charlotte, NC and Meridian, MS

I asked that the very bottom of the BUSINESS CARD TO SAY "Offices in California, North Carolina, Alabama and Mississippi NOT STATES WHERE I AM LICENSED. I.E., I AM NOT LICENSED IN NOTH CAROLINA I NEED NEW FILES IF YOU CAN GET THEM IN THE MORNING MY TIME. WHERE CAN I FIND THE NEW FILES ONCE YOU MODIFY.

for North Carolina, I need an asterick where it is listed. "not licensed will associate counsel" AGAIN NORTH CAROLINA IS 2 WORDS WITH A SPACE BETWEEN THEM

For Biz card, put tollfree number (888)555-0129 and toll free fax (800)555-0147 somewhere like below my cell number or wherever you can. States where I have offices at the bottom: California, North Carolina, Alabama and Mississippi.

For Biz card, put tollfree number (888)555-0129 and toll free fax (800)555-0147 somewhere like below my cell number or wherever you can. States where I have offices at the bottom: California, North Carolina, Alabama and Mississippi. AstericK *North Carolina--not licensed will associate co-counel. Same with letterhead and website. I need to disclose not licensed to practice in North Carolina.

```html
<!DOCTYPE html>
<html lang="en">
<head>
<meta charset="utf-8">
<title>Thorne Legal PC — Business Card</title>
<link rel="stylesheet" href="https://fonts.googleapis.com/css2?family=Roboto+Condensed:wght@300;400&display=swap">
<style>
  :root {
    --stage: #ececec;
    --card-red: #e3202a;
    --ink: #111111;
    --paper: #ffffff;
    --fog-light: #d9d9d9;
    --fog-mid: #a8a8a8;
    --steel-dark: #4a4a4a;
    --steel-deep: #2e2e2e;
    --dash: rgba(255,255,255,0.9);
  }
  * { box-sizing: border-box; margin: 0; padding: 0; }
  html, body {
    width: 1200px; height: 900px; overflow: hidden;
    background: var(--stage);
    font-family: "Roboto Condensed", "Arial Narrow", sans-serif;
  }
  .stage {
    width: 1200px; height: 900px;
    display: flex; align-items: center; justify-content: center;
  }
  .card {
    position: relative;
    width: 1050px; height: 600px;
    overflow: hidden;
    box-shadow: 0 6px 24px rgba(0,0,0,0.18);
  }
  .card__scene {
    position: absolute; inset: 0;
    background: linear-gradient(200deg, var(--fog-light) 0%, var(--fog-light) 35%, var(--fog-mid) 62%, var(--steel-dark) 100%);
  }
  .firm { position: absolute; left: 44px; top: 56px; }
  .firm__name {
    display: flex; align-items: center; gap: 14px;
    font-weight: 300; font-size: 52px; letter-spacing: 1px;
    color: var(--ink); text-transform: uppercase; line-height: 1;
  }
  .firm__mark { width: 14px; height: 14px; background: var(--ink); }
  .firm__practice {
    margin-top: 6px;
    font-weight: 400; font-size: 26px; color: var(--card-red);
  }
  .attorney {
    position: absolute; right: 0; top: 44px;
    display: flex; flex-direction: column; align-items: flex-end;
  }
  .attorney__name {
    background: var(--card-red); color: var(--paper);
    font-weight: 400; font-size: 52px; line-height: 1;
    padding: 10px 26px 10px 22px; text-transform: uppercase;
    letter-spacing: -0.5px;
  }
  .attorney__title {
    background: var(--card-red); color: var(--paper);
    font-weight: 300; font-size: 24px; line-height: 1;
    padding: 6px 28px 8px 20px;
    margin-right: 40px;
    border-top: 2px dashed var(--dash);
  }
  .contact {
    position: absolute; right: 0; top: 226px;
    list-style: none;
    display: flex; flex-direction: column; align-items: flex-end;
  }
  .contact__item {
    background: var(--card-red); color: var(--paper);
    font-weight: 300; font-size: 28px; line-height: 1;
    padding: 7px 22px 8px 16px;
    border-bottom: 2px dashed var(--dash);
  }
  .contact__label { font-size: 20px; margin-right: 8px; }
  .offices {
    position: absolute; left: 0; right: 0; bottom: 0;
    background: var(--steel-deep); color: var(--paper);
    padding: 12px 44px 14px;
    border-top: 4px solid var(--card-red);
    display: flex; justify-content: space-between; align-items: baseline;
  }
  .offices__states { font-weight: 400; font-size: 22px; }
  .offices__note { font-weight: 300; font-size: 17px; }
  .offices__star { color: var(--card-red); }
</style>
</head>
<body>
<main class="stage">
  <article class="card">
    <div class="card__scene" role="img" aria-label="Grayscale sketch-style view of the Harbor Arch Span bridge fading into fog"></div>

    <header class="firm">
      <div class="firm__name"><span>Thorne Legal PC</span><span class="firm__mark"></span></div>
      <p class="firm__practice">Public Claim Advocacy</p>
    </header>

    <section class="attorney">
      <h1 class="attorney__name">H. Dwight Thorne</h1>
      <p class="attorney__title">Attorney</p>
    </section>

    <ul class="contact">
      <li class="contact__item"><span class="contact__label">Cell</span>205/555-0194</li>
      <li class="contact__item"><span class="contact__label">Toll Free</span>(888)555-0129</li>
      <li class="contact__item"><span class="contact__label">Toll Free Fax</span>(800)555-0147</li>
      <li class="contact__item">dwight@thornelegalpc.example</li>
      <li class="contact__item">www.thornelegalpc.example</li>
    </ul>

    <footer class="offices">
      <p class="offices__states">Offices in California, North Carolina<span class="offices__star">*</span>, Alabama and Mississippi</p>
      <p class="offices__note"><span class="offices__star">*</span>North Carolina — not licensed; will associate co-counsel</p>
    </footer>
  </article>
</main>
</body>
</html>
```